Label design needed for cafe display

Hi,
We need a label designed so that we can label food in our display fridge.
The label would have to be editable, as we have lot's of different food items.. and we change the items often, so I would be constantly updating the labels. I will then be printing each label, and laminating them, then displaying them in our food display fridge.
We would like the label to contain our logo - which I have attached.
I have also attached our menus, so you can get a feel for the designs we like.
An example of what we need on a label:
QUICHE LORRAINE $7.50
With Salad $9.50
Please feel free to ask me any questions.
Printing

```html
<!DOCTYPE html>
<html lang="en">
<head>
<meta charset="utf-8">
<title>Display Fridge Label – Quiche Lorraine</title>
<link rel="stylesheet" href="https://fonts.googleapis.com/css2?family=Caprasimo&display=swap">
<style>
  :root {
    --ink-black: #000000;
    --frame-brown: #524548;
    --logo-cream: #fef5b8;
    --panel-charcoal: #231f20;
    --text-white: #ffffff;
    --accent-yellow: #f4ec98;
  }
  html, body {
    margin: 0;
    padding: 0;
    overflow: hidden;
    background: var(--ink-black);
  }
  .label-canvas {
    position: relative;
    width: 1200px;
    height: 360px;
    background: var(--ink-black);
    overflow: hidden;
  }
  .label-frame {
    position: absolute;
    left: 30px;
    top: 30px;
    width: 1140px;
    height: 300px;
    background: var(--frame-brown);
  }
  .brand-tile {
    position: absolute;
    left: 29px;
    top: 28px;
    width: 271px;
    height: 238px;
    background: var(--logo-cream);
    display: flex;
    align-items: center;
    justify-content: center;
  }
  .brand-disc {
    width: 228px;
    height: 228px;
    border-radius: 50%;
    background: var(--frame-brown);
    display: flex;
    align-items: center;
    justify-content: center;
  }
  .brand-name {
    margin: 0;
    font-family: "Caprasimo", serif;
    font-weight: 400;
    font-size: 26px;
    line-height: 1.25;
    letter-spacing: 2px;
    text-align: center;
    color: var(--logo-cream);
  }
  .menu-panel {
    position: absolute;
    left: 330px;
    top: 28px;
    width: 774px;
    height: 238px;
    background: var(--panel-charcoal);
    border: 3px solid var(--text-white);
  }
  .item-name,
  .item-option {
    position: absolute;
    right: 106px;
    margin: 0;
    font-family: "Caprasimo", serif;
    font-weight: 400;
    white-space: nowrap;
  }
  .item-name {
    top: 60px;
    font-size: 44px;
    line-height: 1;
    color: var(--text-white);
  }
  .item-option {
    top: 128px;
    font-size: 35px;
    line-height: 1;
    font-style: italic;
    color: var(--accent-yellow);
  }
</style>
</head>
<body>
  <main class="label-canvas">
    <section class="label-frame">
      <div class="brand-tile">
        <div class="brand-disc">
          <p class="brand-name">REMEDY<br>KITCHEN</p>
        </div>
      </div>
      <div class="menu-panel">
        <h1 class="item-name">QUICHE LORRAINE -$ 7</h1>
        <p class="item-option">W/SALAD -$ 9</p>
      </div>
    </section>
  </main>
</body>
</html>
```